Escrow Accounting firm needs a website design for a startup that services clients nationally.

I offer escrow accounting services for title companies and real estate attorneys. I've enclosed a logo, color palette and flyers with content that can be used for the site.

I'm looking for a similar design concept as the website below from my former employer. Please don't copy because of copyright infringement. Including for design ideas only.
www.harborlinefiduciary.com

Below is a brief write-up...
For professionals in the title insurance industry, finding a trustworthy and budget-friendly solution for escrow accounting can be daunting. When choosing the right accounting partner, title companies and law firms need a group they can rely on, and that's where we come in.

```html
<!DOCTYPE html>
<html lang="en">
<head>
<meta charset="utf-8">
<title>Keystead Escrow Solutions</title>
<link href="https://fonts.googleapis.com/css2?family=Marcellus&family=Nunito+Sans:wght@400;600;700&family=Montserrat:wght@600;700&display=swap" rel="stylesheet">
<style>
:root{
  --navy:#333a47;
  --navy-card:#363e4d;
  --terra:#b87560;
  --terra-light:#c07a64;
  --white:#ffffff;
  --ink:#3a3f4a;
  --muted:#6a6f78;
  --line:#d9dbe0;
}
*{margin:0;padding:0;box-sizing:border-box}
html,body{width:1200px;height:2508px;overflow:hidden}
body{position:relative;background:var(--navy);font-family:"Nunito Sans",sans-serif;color:var(--white)}
.abs{position:absolute}
.serif{font-family:"Marcellus",serif;font-weight:400}
.btn{position:absolute;background:var(--terra);color:var(--white);font-family:"Montserrat",sans-serif;font-weight:700;font-size:10px;letter-spacing:.6px;display:flex;align-items:center;justify-content:center;text-transform:uppercase}
.label{position:absolute;color:var(--terra);font-size:12px;font-weight:600;text-transform:uppercase}
.photo{position:absolute}

/* header */
.header{left:0;top:0;width:1200px;height:92px;background:var(--navy)}
.logo-box{left:211px;top:0;width:166px;height:56px;background:var(--white);display:flex;align-items:center;padding-left:18px;gap:8px}
.logo-mark{width:14px;height:14px;background:var(--terra)}
.logo-text{color:var(--terra);font-family:"Nunito Sans",sans-serif;font-weight:700;line-height:1}
.logo-text .big{font-size:19px;letter-spacing:.5px;display:block}
.logo-text .small{font-size:7.5px;letter-spacing:.8px;display:block;margin-top:2px}
.topinfo{top:13px;display:flex;gap:10px;align-items:center;font-size:9px;line-height:14px;color:var(--white)}
.topinfo svg{width:16px;height:16px}
.nav{left:223px;top:67px;display:flex;gap:36px;font-size:10.5px;font-weight:600;text-transform:uppercase;letter-spacing:.3px}

/* hero */
.hero{left:0;top:92px;width:1200px;height:493px;background:linear-gradient(90deg,#8a8580 0%,#cfcbc6 30%,#5a5550 55%,#e6e2dc 75%,#d8d2ca 100%)}
.hero-panel{left:35px;top:294px;width:726px;height:263px;background:rgba(51,58,71,.88)}
.hero-title{left:125px;top:330px;font-size:38px;line-height:46px}
.hero-text{left:128px;top:424px;width:470px;font-size:9.6px;line-height:15.2px}

/* cards */
.card{top:557px;height:287px;padding:0}
.card .icon{position:absolute;left:55px;top:33px}
.card h3{position:absolute;left:48px;top:96px;font-size:17px;line-height:21px;letter-spacing:.4px}
.card p{position:absolute;left:41px;top:161px;width:300px;font-size:9.4px;line-height:15.2px}
.card .arrow{position:absolute;right:30px;bottom:16px}
.card-1{left:8px;width:387px;background:var(--navy-card)}
.card-2{left:405px;width:386px;background:var(--terra-light)}
.card-3{left:801px;width:389px;background:var(--white);color:var(--ink)}
.card-3 h3{color:var(--ink);top:92px}
.card-3 p{color:var(--muted);top:159px}

/* about */
.about-block{left:205px;top:889px;width:344px;height:313px;background:var(--terra)}
.about-back{left:513px;top:1247px;width:60px;height:59px;background:var(--white)}
.about-photo{left:253px;top:919px;width:306px;height:377px;background:linear-gradient(160deg,#c9c9c5,#9a9893 45%,#2f3b5e 85%)}
.exp-box{left:454px;top:1043px;width:124px;height:115px;background:var(--white);color:var(--ink);text-align:center}
.exp-box .num{font-family:"Marcellus",serif;font-size:36px;margin-top:26px;display:block}
.exp-box .cap{font-size:9.5px;color:var(--muted);margin-top:4px;display:block}
.about-title{left:617px;top:985px;font-size:24px;line-height:29px;letter-spacing:.4px}
.about-text{left:604px;top:1055px;width:410px;font-size:9.5px;line-height:15.2px}

/* why */
.why-photo{left:577px;top:1346px;width:623px;height:331px;background:linear-gradient(100deg,#e4e4e2 0%,#bcc2cc 35%,#8a6a4e 70%,#ded9d4 100%)}
.why-title{left:211px;top:1437px;font-size:24px}
.why-text{left:197px;top:1487px;width:340px;font-size:9.6px;line-height:15.2px}

/* contact */
.contact{left:0;top:1677px;width:1200px;height:320px;background:var(--white);color:var(--ink)}
.contact-title{left:222px;top:1762px;font-size:24px;color:var(--ink)}
.contact-text{left:207px;top:1807px;width:385px;font-size:9.6px;line-height:15.2px;color:var(--muted)}
.info-row{left:208px;display:flex;align-items:center;gap:14px;font-size:9.6px;color:var(--muted)}
.field{border-bottom:1px solid var(--line);height:22px;display:flex;align-items:flex-start;gap:7px;font-size:7px;color:#8b8f96;padding-top:4px}
.field svg{width:9px;height:9px}
.send{left:670px;top:1915px;width:97px;height:33px;background:var(--terra);color:var(--white);display:flex;align-items:center;justify-content:center;gap:10px;font-size:12px;font-weight:600;border-top:4px solid #a6a080}
.agree{left:782px;top:1923px;font-size:6.5px;color:var(--muted);display:flex;align-items:center;gap:5px}
.agree i{width:7px;height:7px;border:1px solid #999;display:inline-block}

/* map */
.map{left:0;top:1997px;width:1200px;height:173px;background:linear-gradient(90deg,#dfe8dc 0%,#e8eaec 35%,#a9c6e8 47%,#a9c6e8 52%,#eceae6 60%,#f0ede6 100%)}

/* footer */
.footer-logo{left:207px;top:2258px;display:flex;align-items:center;gap:10px}
.footer-logo .sq{width:26px;height:26px;background:var(--white)}
.footer-logo .name{font-weight:600;color:var(--white);line-height:1}
.footer-logo .name .big{font-size:27px;letter-spacing:.6px;display:block}
.footer-logo .name .small{font-size:11px;letter-spacing:1.4px;display:block;margin-top:2px}
.footer-text{left:212px;top:2316px;width:220px;font-size:9.6px;line-height:15.2px}
.social{top:2361px;width:16px;height:16px;border:1px solid var(--white);border-radius:50%}
.f-head{font-family:"Montserrat",sans-serif;font-weight:600;font-size:11.5px;letter-spacing:.3px;text-transform:uppercase}
.f-list{font-size:9.6px;line-height:15.2px;list-style:none}
.bottom-bar{left:0;top:2466px;width:1200px;height:42px;background:var(--terra);font-size:9.6px;padding:18px 0 0 208px}
</style>
</head>
<body>

<!-- header -->
<div class="abs header"></div>
<div class="abs logo-box">
  <span class="logo-mark"></span>
  <span class="logo-text"><span class="big">KEYSTEAD</span><span class="small">ESCROW SOLUTIONS</span></span>
</div>
<div class="abs topinfo" style="left:548px">
  <svg viewBox="0 0 24 24" fill="none" stroke="#fff" stroke-width="1.4"><path d="M5 3h4l2 5-2.5 1.5a11 11 0 0 0 6 6L16 13l5 2v4a2 2 0 0 1-2 2A16 16 0 0 1 3 5a2 2 0 0 1 2-2z"/></svg>
  <div>Phone number:<br>(555) 014-2290</div>
</div>
<div class="abs topinfo" style="left:684px">
  <svg viewBox="0 0 24 24" fill="none" stroke="#fff" stroke-width="1.4"><circle cx="12" cy="12" r="9"/><path d="M12 7v5l3 2"/></svg>
  <div>hello@keysteadmail.com<br>Visit Us: 8.00 AM - 6.00 PM</div>
</div>
<div class="abs topinfo" style="left:851px">
  <svg viewBox="0 0 24 24" fill="none" stroke="#fff" stroke-width="1.4"><path d="M12 21s-6-6-6-11a6 6 0 0 1 12 0c0 5-6 11-6 11z"/><circle cx="12" cy="10" r="2"/></svg>
  <div>Address Center<br>4820 Harmon Ave, LA, CA 900</div>
</div>
<nav class="abs nav"><span>Home</span><span>About Us</span><span>Our Services</span><span>Contact Us</span></nav>
<div class="btn" style="left:871px;top:55px;width:151px;height:38px">Request a Quote</div>

<!-- hero -->
<div class="photo hero" role="img" aria-label="Three colleagues reviewing escrow documents together in an office"></div>
<div class="abs hero-panel"></div>
<h1 class="abs serif hero-title">Trusted Escrow<br>Accounting Solutions</h1>
<p class="abs hero-text">Navigating the complexities of escrow accounting in the title insurance industry requires precision, reliability, and trust. Our dedicated team specializes in providing cost-effective and dependable escrow accounting services tailored for title companies and real estate attorneys.</p>
<div class="btn" style="left:127px;top:497px;width:151px;height:38px">Learn More</div>

<!-- service cards -->
<div class="abs card card-1">
  <svg class="icon" width="60" height="50" viewBox="0 0 60 50"><rect x="0" y="0" width="24" height="30" fill="#b87560"/><rect x="12" y="6" width="28" height="36" fill="none" stroke="#fff" stroke-width="1.5"/><text x="16" y="22" fill="#fff" font-size="13" font-family="Nunito Sans,sans-serif">$</text><path d="M26 14h10M26 20h10M18 30h16M18 35h12" stroke="#fff" stroke-width="1.3"/><circle cx="42" cy="40" r="6" fill="#363e4d" stroke="#fff" stroke-width="1.3"/><path d="M39 40l2 2 4-4" stroke="#fff" stroke-width="1.3" fill="none"/></svg>
  <h3 class="serif">Escrow Reconciliation<br>Services</h3>
  <p>Accurate and timely reconciliation is critical in managing escrow accounts. Our Escrow Reconciliation Services ensure that all transactions are thoroughly reviewed and balanced, helping you maintain compliance and avoid costly errors. We provide detailed reports and insights to keep your financials in check and your business running smoothly.</p>
  <svg class="arrow" width="18" height="10" viewBox="0 0 18 10"><path d="M0 5h17M12 1l4 4-4 4" stroke="#fff" stroke-width="1.3" fill="none"/></svg>
</div>
<div class="abs card card-2">
  <svg class="icon" width="60" height="50" style="left:45px;top:30px" viewBox="0 0 60 50"><rect x="0" y="0" width="28" height="34" fill="#fff"/><path d="M16 14c6-3 10-3 14 0v28c-4-3-8-3-14 0zM30 14c6-3 10-3 14 0v28c-4-3-8-3-14 0z" fill="none" stroke="#333a47" stroke-width="1.4"/><path d="M20 8v26M24 6v24" stroke="#333a47" stroke-width="1.3"/><path d="M34 22h7M34 27h7M34 32h7" stroke="#333a47" stroke-width="1.1"/></svg>
  <h3 class="serif" style="left:41px">Best Practices<br>Certification</h3>
  <p>Stay ahead in the industry with our Best Practices Certification service. We help title companies and real estate attorneys adhere to industry standards by providing rigorous evaluations and certifications. This service not only ensures compliance but also enhances your credibility with clients and partners.</p>
  <svg class="arrow" width="18" height="10" viewBox="0 0 18 10"><path d="M0 5h17M12 1l4 4-4 4" stroke="#fff" stroke-width="1.3" fill="none"/></svg>
</div>
<div class="abs card card-3">
  <svg class="icon" width="60" height="50" style="left:48px;top:31px" viewBox="0 0 60 50"><rect x="0" y="0" width="24" height="30" fill="#b87560"/><circle cx="32" cy="22" r="5" fill="none" stroke="#333a47" stroke-width="1.4"/><path d="M22 44c0-8 4-12 10-12s10 4 10 12z" fill="none" stroke="#333a47" stroke-width="1.4"/><path d="M22 6l2 3 3 .5-2 2 .5 3-3.5-1.5-3.5 1.5.5-3-2-2 3-.5zM34 6l2 3 3 .5-2 2 .5 3-3.5-1.5-3.5 1.5.5-3-2-2 3-.5zM46 6l2 3 3 .5-2 2 .5 3-3.5-1.5-3.5 1.5.5-3-2-2 3-.5z" fill="none" stroke="#333a47" stroke-width="1.1"/></svg>
  <h3 class="serif" style="left:42px">Customized Review<br>Services</h3>
  <p style="left:35px">Every business has unique needs, and our Customized Review Services are designed to address them. Whether you require a one-time audit or ongoing support, we tailor our review services to match your specific requirements. Our experts provide thorough and insightful analyses, helping you optimize your escrow processes and safeguard your financial health.</p>
  <svg class="arrow" width="18" height="10" viewBox="0 0 18 10"><path d="M0 5h17M12 1l4 4-4 4" stroke="#b87560" stroke-width="1.3" fill="none"/></svg>
</div>

<!-- about -->
<div class="abs about-block"></div>
<div class="abs about-back"></div>
<div class="photo about-photo" role="img" aria-label="Smiling escrow accountant seated on stone steps outdoors"></div>
<div class="abs exp-box"><span class="num">15</span><span class="cap">Years of experience</span></div>
<div class="label" style="left:619px;top:962px">About Us?</div>
<h2 class="abs serif about-title">Your Reliable Partner<br>in Escrow Accounting</h2>
<p class="abs about-text">Choosing the right escrow accounting partner is crucial for ensuring your business operates smoothly and efficiently. We understand the unique challenges faced by title companies and real estate attorneys, and we're here to provide tailored solutions that meet your needs. With our expertise, attenztion to detail, and commitment to client satisfaction, you can trust us to manage your escrow accounting with precision and professionalism.</p>
<div class="btn" style="left:601px;top:1165px;width:151px;height:38px">About Us</div>

<!-- why -->
<div class="photo why-photo" role="img" aria-label="Two women working closely over paperwork at a desk"></div>
<div class="label" style="left:213px;top:1416px">Why Us</div>
<h2 class="abs serif why-title">Why choose us?</h2>
<p class="abs why-text">We recognize the distinct challenges faced by title companies and real estate attorneys, and we are dedicated to offering customized solutions that address your specific needs. With our deep expertise, meticulous attention to detail, and unwavering commitment to client</p>
<div class="btn" style="left:197px;top:1570px;width:151px;height:38px">Services</div>

<!-- contact -->
<div class="abs contact"></div>
<div class="label" style="left:223px;top:1742px">Contact Us</div>
<h2 class="abs serif contact-title">Get in touch !</h2>
<p class="abs contact-text">Reach out to us today, and let’s discuss how our specialized services can support your business needs. We’re here to provide the solutions you need to succeed.</p>
<div class="abs info-row" style="top:1862px"><svg width="12" height="15" viewBox="0 0 12 15"><path d="M6 15S0 9 0 6a6 6 0 0 1 12 0c0 3-6 9-6 9z" fill="#333a47"/><circle cx="6" cy="6" r="2" fill="#fff"/></svg><span>88 Linden Row, New York, NY 1020 US.</span></div>
<div class="abs info-row" style="top:1889px"><svg width="16" height="13" viewBox="0 0 24 24"><path d="M5 2h4l2 5-2.5 1.5a11 11 0 0 0 6 6L16 12l5 2v4a2 2 0 0 1-2 2A17 17 0 0 1 3 4a2 2 0 0 1 2-2z" fill="#333a47"/></svg><span>(555) 014-2290</span></div>
<div class="abs info-row" style="top:1913px"><svg width="16" height="12" viewBox="0 0 16 12"><rect width="16" height="12" fill="#333a47"/><path d="M0 1l8 6 8-6" stroke="#fff" stroke-width="1.2" fill="none"/></svg><span>info@keysteades.com</span></div>

<div class="abs field" style="left:669px;top:1757px;width:146px"><svg viewBox="0 0 10 10" fill="none" stroke="#8b8f96"><circle cx="5" cy="3" r="2"/><path d="M1 10c0-3 2-4 4-4s4 1 4 4"/></svg>Name</div>
<div class="abs field" style="left:829px;top:1757px;width:145px"><svg viewBox="0 0 10 10" fill="none" stroke="#8b8f96"><rect x=".5" y="2" width="9" height="6"/><path d="M.5 2l4.5 3 4.5-3"/></svg>Email Address</div>
<div class="abs field" style="left:669px;top:1799px;width:146px"><svg viewBox="0 0 10 10" fill="none" stroke="#8b8f96"><path d="M2 1h2l1 2-1 1a5 5 0 0 0 2 2l1-1 2 1v2a1 1 0 0 1-1 1A8 8 0 0 1 1 2a1 1 0 0 1 1-1z"/></svg>Phone</div>
<div class="abs field" style="left:829px;top:1799px;width:145px"><svg viewBox="0 0 10 10" fill="none" stroke="#8b8f96"><circle cx="5" cy="5" r="4.3"/><path d="M5 4v3.5M5 2.5v.5"/></svg>Subject</div>
<div class="abs field" style="left:669px;top:1841px;width:305px;height:46px"><svg viewBox="0 0 10 10" fill="none" stroke="#8b8f96"><path d="M1 9l1-3 5-5 2 2-5 5z"/></svg>How can we help you? Feel free to get in touch!</div>
<div class="abs send"><svg width="16" height="14" viewBox="0 0 16 14" fill="none" stroke="#fff" stroke-width="1.2"><path d="M1 6l14-5-4 12-3-5zM8 8l7-7"/></svg>Send</div>
<div class="abs agree"><i></i>I agree that my data is <u>collected and stored</u>.</div>

<!-- map -->
<div class="photo map" role="img" aria-label="Street map showing the office location"></div>

<!-- footer -->
<div class="abs footer-logo"><span class="sq"></span><span class="name"><span class="big">KEYSTEAD</span><span class="small">ESCROW SOLUTIONS</span></span></div>
<p class="abs footer-text">Reach out to us today, and let’s discuss how our specialized services!</p>
<span class="abs social" style="left:212px"></span>
<span class="abs social" style="left:238px"></span>
<div class="abs f-head" style="left:455px;top:2286px">Navigation</div>
<ul class="abs f-list" style="left:455px;top:2316px"><li>Home</li><li>About Us</li><li>Our Services</li><li>Contact Us</li></ul>
<div class="abs f-head" style="left:595px;top:2286px">Services</div>
<ul class="abs f-list" style="left:595px;top:2316px"><li>Escrow Reconciliation Services</li><li>Best Practices Certification</li><li>Customized Review Services</li></ul>
<div class="abs bottom-bar">Keystead Escrow Solutions © 2024. All Rights Reserved.</div>

</body>
</html>
```